New Business Card Design Project

Target Market(s)

Passing cards out

Industry/Entity Type

Asphalt contractor

Contact Information for Business Card

Ridgefold Paving

Colors
FFC000
F8CF3A
FAE287
FDF2CF
FEFAEE
F0912C
F2A743
F7CA91
FBE8D2
FDF5EE
EE7325
F08F49
F5BC92
FAE3D3
FDF4ED

Requirements
Must have
• Asphalt
Nice to have
• Would like to have 2 pictures on it of equipment

```html
<!DOCTYPE html>
<html lang="en">
<head>
<meta charset="utf-8">
<title>Ridgefold Paving – Business Cards</title>
<link href="https://fonts.googleapis.com/css2?family=Exo+2:ital,wght@0,700;0,800;1,800&family=Lobster&family=Rubik:wght@700&display=swap" rel="stylesheet">
<style>
  :root {
    --backdrop: #1c1c1c;
    --card-yellow: #ffc000;
    --brand-red: #e8100e;
    --band-black: #000000;
    --ink: #111111;
    --white: #ffffff;
    --photo-light: #d9d9d6;
    --photo-mid: #9a9a96;
  }
  * { box-sizing: border-box; margin: 0; padding: 0; }
  html, body { width: 1200px; height: 1059px; overflow: hidden; background: var(--backdrop); }
  .canvas { position: relative; width: 1200px; height: 1059px; }

  .card { position: absolute; background: var(--card-yellow); border-radius: 30px; overflow: hidden; }
  .card-front { left: 241px; top: 95px; width: 712px; height: 406px; }
  .card-back { left: 234px; top: 529px; width: 741px; height: 424px; border-radius: 36px; }

  .tagline {
    position: absolute; top: 12px; left: 0; width: 100%; text-align: center;
    font-family: "Lobster", cursive; font-size: 46px; color: var(--brand-red); letter-spacing: 1px;
  }
  .equipment-photo {
    position: absolute; left: 0; top: 72px; width: 335px; height: 178px;
    background: radial-gradient(ellipse at 45% 50%, var(--photo-light) 0%, var(--photo-mid) 55%, rgba(255,192,0,0) 85%);
  }
  .brand-name {
    font-family: "Exo 2", sans-serif; font-weight: 800; color: var(--brand-red);
    text-transform: uppercase; text-align: center; line-height: 0.95;
  }
  .card-front .brand-block {
    position: absolute; left: 345px; top: 92px; width: 355px; height: 150px;
    display: flex; flex-direction: column; justify-content: center;
  }
  .card-front .brand-name .line-main { display: block; font-size: 56px; }
  .card-front .brand-name .line-sub { display: block; font-size: 40px; margin-top: 6px; }

  .services-band {
    position: absolute; left: 0; top: 245px; width: 100%; height: 110px;
    background: var(--band-black); text-align: center;
    font-family: "Exo 2", sans-serif; font-weight: 800; font-style: italic;
  }
  .services-band .specialty { color: var(--brand-red); font-size: 24px; margin-top: 7px; }
  .services-band .service-list { color: var(--white); font-size: 24px; line-height: 31px; }

  .contact-row {
    position: absolute; left: 28px; right: 28px; top: 365px;
    display: flex; align-items: center; justify-content: space-between;
    font-family: "Rubik", sans-serif; font-weight: 700; color: var(--ink);
  }
  .contact-item { display: flex; align-items: center; gap: 6px; }
  .contact-item.phone { font-size: 19px; }
  .contact-item.web { font-size: 16px; }
  .contact-item svg { flex: none; }

  .card-back .brand-block {
    position: absolute; left: 0; top: 60px; width: 100%; height: 230px;
    display: flex; flex-direction: column; justify-content: center;
  }
  .card-back .brand-name .line-main { display: block; font-size: 92px; }
  .card-back .brand-name .line-sub { display: block; font-size: 60px; margin-top: 10px; }
  .card-back .web-line {
    position: absolute; left: 0; width: 100%; top: 338px;
    display: flex; align-items: center; justify-content: center; gap: 12px;
    font-family: "Rubik", sans-serif; font-weight: 700; font-size: 32px; color: var(--brand-red);
  }
</style>
</head>
<body>
<div class="canvas">

  <section class="card card-front">
    <p class="tagline">Doing It Right Since 1992</p>
    <div class="equipment-photo" role="img" aria-label="Photo of a white asphalt distributor truck"></div>
    <div class="brand-block">
      <p class="brand-name"><span class="line-main">Ridgefold</span><span class="line-sub">Paving</span></p>
    </div>
    <div class="services-band">
      <p class="specialty">Specialist in Chipseal &amp; Hotmix</p>
      <p class="service-list">Ranch Roads &nbsp;•&nbsp; City Streets • &nbsp;Sub Divisions</p>
      <p class="service-list">• &nbsp;Patching • &nbsp;Driveways &nbsp;• &nbsp;Parking Lots</p>
    </div>
    <div class="contact-row">
      <span class="contact-item phone">
        <svg width="20" height="20" viewBox="0 0 24 24" aria-hidden="true"><path fill="none" stroke="currentColor" stroke-width="2.4" stroke-linejoin="round" d="M5 3h4l2 5-2.5 1.5a11 11 0 0 0 6 6L16 13l5 2v4a2 2 0 0 1-2 2A16 16 0 0 1 3 5a2 2 0 0 1 2-2z"/></svg>
        555-214-7730, 555-386-1029
      </span>
      <span class="contact-item web">
        <svg width="22" height="22" viewBox="0 0 24 24" aria-hidden="true"><circle cx="12" cy="12" r="10" fill="none" stroke="currentColor" stroke-width="2.2"/><path fill="none" stroke="currentColor" stroke-width="1.6" d="M2 12h20M12 2c3 3 3 17 0 20M12 2c-3 3-3 17 0 20"/></svg>
        &nbsp;www.ridgefoldpaving@example.com
      </span>
    </div>
  </section>

  <section class="card card-back">
    <div class="brand-block">
      <p class="brand-name"><span class="line-main">Ridgefold</span><span class="line-sub">Paving</span></p>
    </div>
    <p class="web-line">
      <svg width="40" height="40" viewBox="0 0 24 24" aria-hidden="true"><circle cx="12" cy="12" r="10" fill="none" stroke="currentColor" stroke-width="2.2"/><path fill="none" stroke="currentColor" stroke-width="1.6" d="M2 12h20M12 2c3 3 3 17 0 20M12 2c-3 3-3 17 0 20"/></svg>
      www.ridgefoldpaving@example.com
    </p>
  </section>

</div>
</body>
</html>
```